Change lives by changing education

We need stationery (business cards, letterhead, envelopes, with compliments slips and A4 display folders) that will support us to make an impact in education through recruitment and consultancy services. All our consultants are highly experienced with more than 20 years of industry experience and are all passionate about improving education by attracting the brightest and the best. We believe strongly in empowering students to take control of their own learning and turn their own ideas into reality.
We work in the independent/private school space which can be thought of as conservative, but they are just starting to "get with the times" and be more progressive, so the message has to carry across that space.We are a younger firm, but one of the few who has experienced educators running the show. Help us to make a difference to the world please!

Target Market(s)

Principals and School Board members

Industry/Entity Type

Business

Requirements
Must have
• The logo
Nice to have
• Use of the logo colours Indigo and a specific type of green
Should not have
• Nothing tacky to do with education, incl quills, pens, mortar boards, books

```html
<!DOCTYPE html>
<html lang="en">
<head>
<meta charset="utf-8">
<title>Brightwell Consulting — Stationery Set</title>
<link rel="stylesheet" href="https://fonts.googleapis.com/css2?family=Cinzel:wght@500&family=Open+Sans:wght@400;600&family=Great+Vibes&display=swap">
<style>
  :root {
    --indigo: #3b356b;
    --green: #5e8a3a;
    --paper: #fbfbfb;
    --backdrop: #ececec;
    --ink: #4a4a55;
    --rule: #b9b9c2;
  }
  * { margin: 0; padding: 0; box-sizing: border-box; }
  html, body { width: 1200px; height: 802px; overflow: hidden; }
  body {
    background: var(--backdrop);
    position: relative;
    font-family: "Open Sans", Arial, sans-serif;
    color: var(--ink);
  }
  .piece { position: absolute; background: var(--paper); box-shadow: 0 2px 6px rgba(0,0,0,.12); }
  .base-band { position: absolute; left: 0; right: 0; bottom: 0; height: 4px; background: var(--indigo); }

  /* wordmark */
  .wordmark { position: absolute; display: flex; align-items: center; gap: 4px; }
  .wordmark__dot { border-radius: 50%; background: var(--green); flex: none; }
  .wordmark__name {
    font-family: "Cinzel", Georgia, serif; font-weight: 500;
    color: var(--indigo); line-height: 1.05; letter-spacing: .02em;
  }
  .wordmark--light .wordmark__name { color: #ffffff; }

  .small { font-size: 4.6px; line-height: 1.55; color: var(--ink); }
  .icon { display: inline-block; width: 4px; height: 4px; background: var(--indigo); border-radius: 1px; margin-right: 2px; vertical-align: -0.5px; }

  /* letterhead */
  .letterhead { left: 186px; top: 100px; width: 294px; height: 418px; }
  .letterhead .wordmark { left: 104px; top: 22px; }
  .letterhead__rule { position: absolute; left: 17px; right: 17px; top: 375px; height: 1px; background: var(--rule); }
  .letterhead__contacts { position: absolute; left: 17px; top: 380px; }
  .letterhead__address { position: absolute; right: 17px; top: 381px; text-align: right; }
  .web { letter-spacing: .12em; }

  /* folder */
  .folder { left: 532px; top: 81px; width: 349px; height: 441px; background: var(--indigo); }
  .folder__spine { position: absolute; left: 6px; top: 0; bottom: 0; width: 8px; border-right: 1px solid rgba(255,255,255,.08); border-left: 1px solid rgba(0,0,0,.12); }
  .folder .wordmark { left: 64px; top: 200px; gap: 10px; }

  /* business cards */
  .card { width: 133px; height: 75px; }
  .card--back { left: 939px; top: 340px; background: var(--indigo); overflow: hidden; }
  .card__artwork { position: absolute; left: 0; top: 0; width: 78px; height: 75px;
    background: linear-gradient(135deg, #eef0f4 0%, var(--green) 45%, var(--indigo) 100%); opacity: .85; }
  .card__details { position: absolute; right: 6px; top: 8px; text-align: right; color: #fff; }
  .card__details .wordmark__name { font-size: 6.5px; color: #fff; }
  .card__person { font-family: "Cinzel", Georgia, serif; font-size: 4.6px; margin-top: 5px; }
  .card__role { font-size: 3.2px; color: #9fc27c; }
  .card__details .small { color: #e6e6f0; font-size: 3.2px; line-height: 1.5; margin-top: 3px; }
  .card--front { left: 939px; top: 437px; }
  .card--front .wordmark { left: 30px; top: 28px; }

  /* envelopes & slip */
  .envelope { width: 330px; height: 159px; top: 566px; }
  .envelope--front { left: 86px; }
  .envelope--front .wordmark { left: 12px; top: 12px; }
  .envelope__return { position: absolute; left: 12px; top: 40px; }
  .envelope--back { left: 449px; width: 331px; }
  .envelope__flap { position: absolute; left: 0; right: 0; top: 0; height: 55px; background: var(--indigo);
    clip-path: polygon(0 0, 100% 0, 100% 100%, 94% 100%, 90% 88%, 10% 88%, 6% 100%, 0 100%); }
  .envelope__flap .wordmark__dot { position: absolute; left: 159px; top: 13px; width: 14px; height: 14px; }
  .envelope__flap .small { position: absolute; left: 0; right: 0; top: 36px; text-align: center; color: #fff; }
  .slip { left: 810px; width: 330px; height: 159px; top: 566px; }
  .slip .wordmark { left: 14px; top: 24px; }
  .slip__contacts { position: absolute; left: 256px; top: 10px; }
  .slip__greeting { position: absolute; left: 90px; top: 103px; font-family: "Great Vibes", cursive; font-size: 25px; color: var(--indigo); }
</style>
</head>
<body>

  <section class="piece letterhead">
    <div class="wordmark"><span class="wordmark__dot" style="width:8px;height:8px"></span><span class="wordmark__name" style="font-size:9px">Brightwell<br>Consulting</span></div>
    <div class="letterhead__rule"></div>
    <div class="letterhead__contacts small">
      <div><span class="icon"></span>555 210 4471</div>
      <div><span class="icon"></span>555 382 9016</div>
      <div><span class="icon"></span>hello@brightwell.co</div>
    </div>
    <div class="letterhead__address small">
      <div>412 Maple Court</div>
      <div>Fairview, Oregon 97024</div>
      <div class="web">www.brightwell.co</div>
    </div>
    <div class="base-band"></div>
  </section>

  <section class="piece folder">
    <div class="folder__spine"></div>
    <div class="wordmark wordmark--light"><span class="wordmark__dot" style="width:26px;height:26px"></span><span class="wordmark__name" style="font-size:24px">Brightwell<br>Consulting</span></div>
  </section>

  <section class="piece card card--back">
    <div class="card__artwork" role="img" aria-label="Tree of leaves illustration in white and green"></div>
    <div class="card__details">
      <div class="wordmark__name">Brightwell<br>Consulting</div>
      <div class="card__person">Clara Voss</div>
      <div class="card__role">Senior Consultant</div>
      <div class="small">
        <div>412 Maple Court</div>
        <div>Fairview, Oregon 97024</div>
        <div>555 210 4471</div>
        <div>555 382 9016</div>
        <div>hello@brightwell.co</div>
        <div>www.brightwell.co</div>
      </div>
    </div>
  </section>

  <section class="piece card card--front">
    <div class="wordmark"><span class="wordmark__dot" style="width:7px;height:7px"></span><span class="wordmark__name" style="font-size:8px">Brightwell<br>Consulting</span></div>
  </section>

  <section class="piece envelope envelope--front">
    <div class="wordmark"><span class="wordmark__dot" style="width:9px;height:9px"></span><span class="wordmark__name" style="font-size:10px">Brightwell<br>Consulting</span></div>
    <div class="envelope__return small">
      <div>412 Maple Court</div>
      <div>Fairview, Oregon 97024</div>
    </div>
    <div class="base-band"></div>
  </section>

  <section class="piece envelope envelope--back">
    <div class="envelope__flap">
      <span class="wordmark__dot"></span>
      <div class="small">www.brightwell.co</div>
    </div>
  </section>

  <section class="piece slip">
    <div class="wordmark"><span class="wordmark__dot" style="width:9px;height:9px"></span><span class="wordmark__name" style="font-size:10px">Brightwell<br>Consulting</span></div>
    <div class="slip__contacts small">
      <div>412 Maple Court</div>
      <div>Fairview, Oregon 97024</div>
      <div><span class="icon"></span>555 210 4471</div>
      <div><span class="icon"></span>555 382 9016</div>
      <div><span class="icon"></span>hello@brightwell.co</div>
      <div><span class="icon"></span>www.brightwell.co</div>
    </div>
    <div class="slip__greeting">With Compliments</div>
    <div class="base-band"></div>
  </section>

</body>
</html>
```